Business cards, Stationary, E-mail signature, leterhead, fax coversheet, thank you card, invoice tem
Torvan Networks Stationary - please read brief
Business cards, Stationary, E-mail signature, leterhead, fax coversheet, thank you card, invoice tem -
Creative Brief
Use specific fonts
Use the best that will go with the logo design
Professional
Brent Oakley
71523 Birch Ridge Court, Suite 204 Sterling, VA 20783
BrentO@torvannetworks.example
www.torvannetworks.example
Use the icon on the left side of the logo only

```html
<!DOCTYPE html>
<html lang="en">
<head>
<meta charset="utf-8">
<title>Torvan Networks Business Cards</title>
<link href="https://fonts.googleapis.com/css2?family=Montserrat:wght@400;600;700&display=swap" rel="stylesheet">
<style>
  :root {
    --bg: #e9e7e4;
    --card: #ffffff;
    --navy: #1c2f6e;
    --blue: #2a5fb8;
    --tab: #3566c4;
    --tab-dark: #1b3a86;
    --grey: #6b6f76;
    --rule: #c9ccd2;
    --mark: #7a8594;
  }
  * { box-sizing: border-box; margin: 0; padding: 0; }
  html, body { width: 1200px; height: 852px; overflow: hidden; }
  body {
    background: var(--bg);
    font-family: "Montserrat", Arial, sans-serif;
    position: relative;
  }
  .card {
    position: absolute;
    width: 520px;
    height: 300px;
    background: var(--card);
    border-radius: 16px;
    box-shadow: 0 6px 18px rgba(0,0,0,.18);
  }
  .card--front { left: 70px; top: 90px; }
  .card--back { left: 610px; top: 462px; }
  .edge-tab {
    position: absolute;
    width: 9px;
    height: 52px;
    background: linear-gradient(90deg, var(--tab-dark), var(--tab));
    border-radius: 4px;
  }
  .edge-tab--left { left: -4px; }
  .edge-tab--right { right: -4px; }
  .brand__dot { width: 62px; height: 62px; border-radius: 50%; background: var(--mark); flex: none; }
  .brand__name {
    font-weight: 700;
    color: var(--navy);
    text-transform: uppercase;
    white-space: nowrap;
  }
  .brand__tagline {
    font-size: 7px;
    letter-spacing: 1.2px;
    color: var(--grey);
    text-transform: uppercase;
    white-space: nowrap;
  }
  .holder__name { font-weight: 700; font-size: 15px; color: var(--blue); margin-bottom: 14px; }
  .holder__address { font-size: 11px; line-height: 1.6; color: var(--grey); }
  .contacts { list-style: none; }
  .contacts li {
    display: flex; align-items: center; gap: 8px;
    font-size: 11px; color: var(--grey); line-height: 1; margin-bottom: 7px;
    white-space: nowrap;
  }
  .contacts svg { width: 12px; height: 12px; flex: none; }
  .divider { position: absolute; width: 1px; background: var(--rule); }

  /* front card */
  .card--front .brand { position: absolute; left: 100px; top: 40px; display: flex; align-items: center; gap: 14px; }
  .card--front .brand__name { font-size: 25px; letter-spacing: 1.5px; }
  .card--front .brand__tagline { position: absolute; left: 176px; top: 98px; }
  .card--front .holder { position: absolute; left: 40px; top: 152px; width: 200px; text-align: right; }
  .card--front .divider { left: 255px; top: 150px; height: 100px; }
  .card--front .contacts { position: absolute; left: 270px; top: 152px; }

  /* back card */
  .card--back .brand {
    position: absolute; left: 14px; top: 74px; width: 196px;
    display: flex; flex-direction: column; align-items: center; gap: 12px;
  }
  .card--back .brand__name { font-size: 16px; letter-spacing: 1px; }
  .card--back .brand__tagline { font-size: 6px; letter-spacing: 1px; margin-top: -6px; }
  .card--back .divider { left: 222px; top: 40px; height: 230px; }
  .card--back .holder { position: absolute; left: 238px; top: 44px; }
  .card--back .contacts { position: absolute; left: 238px; top: 160px; }
</style>
</head>
<body>

<svg width="0" height="0" style="position:absolute" aria-hidden="true">
  <defs>
    <symbol id="icon-phone" viewBox="0 0 24 24"><path fill="#1c2f6e" d="M6.6 10.8a15.2 15.2 0 0 0 6.6 6.6l2.2-2.2a1 1 0 0 1 1-.25 11.4 11.4 0 0 0 3.6.57 1 1 0 0 1 1 1V20a1 1 0 0 1-1 1A17 17 0 0 1 3 4a1 1 0 0 1 1-1h3.5a1 1 0 0 1 1 1c0 1.25.2 2.45.57 3.57a1 1 0 0 1-.25 1z"/></symbol>
    <symbol id="icon-fax" viewBox="0 0 24 24"><path fill="#1c2f6e" d="M6 2h12v6H6zM3 9h18a1 1 0 0 1 1 1v7h-4v5H6v-5H2v-7a1 1 0 0 1 1-1zm5 7v4h8v-4z"/></symbol>
    <symbol id="icon-email" viewBox="0 0 24 24"><circle cx="12" cy="12" r="10" fill="#1c2f6e"/><text x="12" y="16.5" font-size="13" font-family="Arial" font-weight="700" fill="#fff" text-anchor="middle">@</text></symbol>
    <symbol id="icon-web" viewBox="0 0 24 24"><circle cx="12" cy="12" r="9.5" fill="none" stroke="#1c2f6e" stroke-width="2"/><path d="M2.5 12h19M12 2.5c-5 5-5 14 0 19M12 2.5c5 5 5 14 0 19" fill="none" stroke="#1c2f6e" stroke-width="1.6"/></symbol>
  </defs>
</svg>

<section class="card card--front">
  <span class="edge-tab edge-tab--left" style="top:200px"></span>
  <span class="edge-tab edge-tab--right" style="top:130px"></span>
  <div class="brand">
    <span class="brand__dot"></span>
    <span class="brand__name">Torvan Networks</span>
  </div>
  <p class="brand__tagline">IT | Management Consulting | Staffing</p>
  <div class="holder">
    <p class="holder__name">Brent Oakley</p>
    <p class="holder__address">71523 Birch Ridge Court,<br>Suite 204, Sterling, VA 20783</p>
  </div>
  <span class="divider"></span>
  <ul class="contacts">
    <li><svg><use href="#icon-phone"/></svg>703 555 0142</li>
    <li><svg><use href="#icon-fax"/></svg>703 555 0148</li>
    <li><svg><use href="#icon-email"/></svg>BrentO@torvannetworks.example</li>
    <li><svg><use href="#icon-web"/></svg>www.torvannetworks.example</li>
  </ul>
</section>

<section class="card card--back">
  <span class="edge-tab edge-tab--left" style="top:180px"></span>
  <span class="edge-tab edge-tab--right" style="top:210px"></span>
  <div class="brand">
    <span class="brand__dot"></span>
    <span class="brand__name">Torvan Networks</span>
    <p class="brand__tagline">IT | Management Consulting | Staffing</p>
  </div>
  <span class="divider"></span>
  <div class="holder">
    <p class="holder__name">Brent Oakley</p>
    <p class="holder__address">71523 Birch Ridge Court,<br>Suite 204, Sterling, VA 20783</p>
  </div>
  <ul class="contacts">
    <li><svg><use href="#icon-phone"/></svg>703 555 0142</li>
    <li><svg><use href="#icon-fax"/></svg>703 555 0148</li>
    <li><svg><use href="#icon-email"/></svg>BrentO@torvannetworks.example</li>
    <li><svg><use href="#icon-web"/></svg>www.torvannetworks.example</li>
  </ul>
</section>

</body>
</html>
```